Investment Company Business Card Design

We need a Business Card design for a new company based in Boston called "Velm Investment". We are cooperating with local real estate and construction companies. Our company is very actively and aggressively acquiring primarily residential investment properties either to buy and hold long term or for purposes or renovating and repositioning for re-sale in the market. In addition, we undertake some development projects and acquisitions as opportunities present themselves. the final design should contains information about “Velm" the river boat. we are tenacious, indomitable, and the business have a favorable wind throughout the voyage for all our investment.
sample Info. on Design:
Tusa Merrick
CEO
555-xxx-xxxx
418 Harlow St. Suite 507, Boston, MA 02111
Please provide a template also, that we can edit the info later.
Reason: i just got new LOGO Design attached will be use in Business Card Design.
Construction

```html
<!DOCTYPE html>
<html lang="en">
<head>
<meta charset="utf-8">
<title>Velm Investment – Business Card</title>
<link rel="stylesheet" href="https://fonts.googleapis.com/css2?family=Exo+2:wght@400;500;600&display=swap">
<style>
  :root {
    --backdrop: #e4e4e6;
    --card: #ffffff;
    --gold: #d6b25e;
    --gold-light: #ecd49a;
    --silver: #b9b9bc;
    --silver-light: #dcdcde;
    --ink: #2a2a2c;
    --ink-soft: #55555a;
    --logo-grey: #8d8d92;
  }
  * { margin: 0; padding: 0; box-sizing: border-box; }
  html, body {
    width: 1200px; height: 900px; overflow: hidden;
    background: var(--backdrop);
    font-family: "Exo 2", sans-serif;
    color: var(--ink);
  }
  .canvas {
    position: relative; width: 1200px; height: 900px;
    display: flex; flex-direction: column; align-items: center; justify-content: center; gap: 40px;
  }
  .card {
    position: relative; width: 665px; height: 380px;
    background: var(--card);
    box-shadow: 0 6px 18px rgba(0,0,0,0.12);
    overflow: hidden;
  }
  .card-swoosh { position: absolute; inset: 0; width: 100%; height: 100%; }
  .brand { position: absolute; text-align: center; }
  .brand-name {
    font-size: 44px; font-weight: 500; letter-spacing: 3px;
    color: var(--logo-grey); line-height: 1;
  }
  .brand-tagline {
    margin-top: 6px; font-size: 10px; letter-spacing: 1.5px;
    color: var(--ink-soft); text-transform: uppercase;
  }
  .card-front .brand { left: 0; right: 0; top: 95px; }
  .card-back .brand { left: 40px; top: 70px; text-align: left; }
  .card-back .brand-name { font-size: 36px; }
  .website-band {
    position: absolute; font-size: 22px; font-weight: 600;
    letter-spacing: 2px; color: var(--ink);
  }
  .card-front .website-band { right: 70px; bottom: 60px; font-size: 20px; }
  .card-back .website-band { right: 60px; bottom: 52px; }
  .person { position: absolute; right: 45px; top: 48px; text-align: right; }
  .person-name { font-size: 22px; font-weight: 500; letter-spacing: 1px; text-transform: uppercase; }
  .person-role {
    font-size: 13px; color: var(--ink-soft); margin-top: 2px;
    padding-bottom: 6px; border-bottom: 1px solid var(--silver-light); padding-left: 60px;
  }
  .address { position: absolute; right: 45px; top: 140px; text-align: right; font-size: 17px; line-height: 1.35; }
  .contact-list {
    position: absolute; left: 50px; top: 175px; list-style: none;
    font-size: 12px; line-height: 21px; color: var(--ink);
    border-top: 1px solid var(--silver-light); padding-top: 8px; width: 190px;
  }
  .contact-list li { display: flex; align-items: center; gap: 10px; }
  .contact-icon { width: 12px; height: 12px; fill: var(--ink); flex: none; }
</style>
</head>
<body>
<main class="canvas">

  <section class="card card-front" aria-label="Card front">
    <svg class="card-swoosh" viewBox="0 0 665 380" aria-hidden="true">
      <defs>
        <linearGradient id="goldFront" x1="0" y1="0" x2="1" y2="0">
          <stop offset="0" stop-color="var(--gold-light)"/>
          <stop offset="1" stop-color="var(--gold)"/>
        </linearGradient>
      </defs>
      <path d="M0,330 Q330,230 665,205 L665,218 Q330,245 0,345 Z" fill="var(--silver)"/>
      <path d="M0,355 Q330,255 665,232 L665,380 L0,380 Z" fill="url(#goldFront)"/>
    </svg>
    <div class="brand">
      <div class="brand-name">VELM INVEST</div>
      <div class="brand-tagline">Residential Investment &amp; Development</div>
    </div>
    <div class="website-band">www.velminvest.com</div>
  </section>

  <section class="card card-back" aria-label="Card back">
    <svg class="card-swoosh" viewBox="0 0 665 380" aria-hidden="true">
      <defs>
        <linearGradient id="goldBack" x1="0" y1="0" x2="1" y2="0">
          <stop offset="0" stop-color="var(--gold-light)"/>
          <stop offset="1" stop-color="var(--gold)"/>
        </linearGradient>
      </defs>
      <path d="M60,380 Q360,235 665,150 L665,162 Q370,250 90,380 Z" fill="var(--silver)"/>
      <path d="M140,380 Q390,255 665,175 L665,380 Z" fill="url(#goldBack)"/>
    </svg>

    <div class="brand">
      <div class="brand-name">VELM INVEST</div>
      <div class="brand-tagline">Residential Investment &amp; Development</div>
    </div>

    <div class="person">
      <div class="person-name">Tusa Merrick</div>
      <div class="person-role">Managing Director</div>
    </div>

    <div class="address">418 Harlow St. Suite 507<br>Boston, MA 02111</div>

    <ul class="contact-list">
      <li><svg class="contact-icon" viewBox="0 0 12 12"><path d="M2 1l2 0 1 3-1.3 1a6 6 0 0 0 3.3 3.3L8 7l3 1v2a1 1 0 0 1-1 1A9 9 0 0 1 1 2a1 1 0 0 1 1-1z"/></svg>555-xxx-xxxx</li>
      <li><svg class="contact-icon" viewBox="0 0 12 12"><path d="M3.5 0h5a1 1 0 0 1 1 1v10a1 1 0 0 1-1 1h-5a1 1 0 0 1-1-1V1a1 1 0 0 1 1-1zM4 1.5v8h4v-8zM6 10a.6.6 0 1 0 0 1.2A.6.6 0 0 0 6 10z"/></svg>555-xxx-xxxx</li>
      <li><svg class="contact-icon" viewBox="0 0 12 12"><path d="M3 0h5v3H3zM1 4h10v6H9v2H3v-2H1zM4 8v3h4V8z"/></svg>555-xxx-xxxx</li>
      <li><svg class="contact-icon" viewBox="0 0 12 12"><path d="M0 2h12v8H0zM1 3l5 4 5-4v-.2H1z" fill-rule="evenodd"/></svg>tusa@velminvest.com</li>
      <li><svg class="contact-icon" viewBox="0 0 12 12"><path d="M6 0a6 6 0 1 0 0 12A6 6 0 0 0 6 0zm0 1.2c.8.9 1.3 2.5 1.4 4.2H4.6C4.7 3.7 5.2 2.1 6 1.2zM1.3 6.6h2.2c.1 1.6.5 3 1.1 3.9A4.8 4.8 0 0 1 1.3 6.6zm0-1.2a4.8 4.8 0 0 1 3.3-3.9C4 2.4 3.6 3.8 3.5 5.4zM6 10.8c-.8-.9-1.3-2.5-1.4-4.2h2.8c-.1 1.7-.6 3.3-1.4 4.2zm1.4-.3c.6-.9 1-2.3 1.1-3.9h2.2a4.8 4.8 0 0 1-3.3 3.9zm1.1-5.1c-.1-1.6-.5-3-1.1-3.9a4.8 4.8 0 0 1 3.3 3.9z"/></svg>www.velminvest.com</li>
    </ul>

    <div class="website-band">www.velminvest.com</div>
  </section>

</main>
</body>
</html>
```